Outdoor kitchen and Appliance Need new business card

We need a new business card, for our business.

Front side with all info, back side with more brand identity.

I have attached some drafts, we moved up but it lacks creativity.

Use https://photos.quendrix.com and I can purchase, the stock photo and send it you if you design is chosen.

We are also planing on printing business card with the logo, having a spot uv. I have attached instructions.

Plumtarvessa.com is our website

Target Market(s)

Extremely high end customer.

Contact Information for Business Card

Double sided with spot uv on logos

Colors
ec1f27

Requirements
Must have
• See sample I have attached, we are open to ideas.

Colors, are: RED, Stainless steel, Black

```html
<!DOCTYPE html>
<html lang="en">
<head>
<meta charset="utf-8">
<title>Plumtarvessa – Business Card</title>
<link rel="stylesheet" href="https://fonts.googleapis.com/css2?family=Open+Sans:ital,wght@0,400;0,600;0,700;1,700;1,800&display=swap">
<style>
  :root {
    --brand-red: #ec1f27;
    --deep-red: #b3161d;
    --black: #0b0b0b;
    --steel: #dcdcdc;
    --paper: #f4f4f4;
    --ink: #1a1a1a;
    --slate: #6e6e6e;
    --backdrop: #c9c9cb;
  }
  * { box-sizing: border-box; margin: 0; padding: 0; }
  html, body {
    width: 1200px; height: 1200px; overflow: hidden;
    background: var(--backdrop);
    font-family: "Open Sans", Arial, sans-serif;
  }
  .stage {
    position: absolute; left: 0; top: 0;
    width: 1000px; height: 1000px;
    transform: scale(1.2); transform-origin: 0 0;
  }
  .card {
    position: absolute; left: 160px; width: 700px; height: 400px; overflow: hidden;
  }
  .card--front {
    top: 76px;
    background: linear-gradient(120deg, var(--brand-red) 0%, #8e1a22 40%, #3a1214 75%, #050505 100%);
  }
  .card--back { top: 518px; background: var(--paper); }

  .brand-name {
    position: absolute;
    font-weight: 700; color: var(--steel); letter-spacing: 2px;
    white-space: nowrap;
  }
  .card--front .brand-name { left: 0; right: 0; top: 178px; text-align: center; font-size: 40px; }
  .card--back .brand-name { left: 420px; width: 260px; top: 188px; text-align: center; font-size: 24px; }

  .card-shapes { position: absolute; inset: 0; width: 700px; height: 400px; }

  .info { position: absolute; left: 68px; top: 30px; }
  .tagline {
    font-style: italic; font-weight: 800; color: var(--slate);
    font-size: 16.5px; line-height: 23px; text-transform: uppercase;
  }
  .tagline span { display: inline-block; border-bottom: 1.5px solid var(--slate); padding-bottom: 1px; }
  .office-label { color: var(--brand-red); font-weight: 600; font-size: 13.5px; margin-top: 3px; }
  .line {
    display: flex; align-items: flex-start; gap: 5px;
    font-size: 14px; line-height: 18.5px; color: var(--ink);
  }
  .line svg { width: 10px; height: 10px; margin-top: 4px; flex: none; fill: var(--brand-red); }
  .address { margin-bottom: 26px; }
  .web { color: var(--brand-red); font-weight: 600; }

  .person { position: absolute; left: 40px; top: 322px; padding-left: 19px; border-left: 7px solid var(--brand-red); }
  .person-name { font-size: 30px; font-weight: 600; color: var(--ink); line-height: 32px; letter-spacing: 0.3px; }
  .person-name em { font-style: normal; color: var(--brand-red); }
  .person-role { font-size: 17px; color: var(--brand-red); line-height: 20px; letter-spacing: 0.4px; }
</style>
</head>
<body>
<main class="stage">

  <section class="card card--front" aria-label="Card front">
    <div class="brand-name">PLUMTARVESSA</div>
  </section>

  <section class="card card--back" aria-label="Card back">
    <svg class="card-shapes" viewBox="0 0 700 400" aria-hidden="true">
      <rect class="edge-strip" x="0" y="0" width="45" height="400" fill="var(--black)"/>
      <polygon class="red-band" points="440,0 505,0 410,200 505,400 460,400 350,195" fill="var(--brand-red)"/>
      <polygon class="red-band-shade" points="350,195 410,200 505,400 460,400" fill="var(--deep-red)"/>
      <polygon class="dark-panel" points="505,0 700,0 700,400 505,400 405,210 412,190" fill="var(--black)"/>
    </svg>

    <div class="info">
      <p class="tagline">Custom built outdoor kitchen<br><span>and appliances</span></p>
      <p class="office-label">OFFICE - SHOWROOM</p>
      <div class="line address">
        <svg viewBox="0 0 10 10"><path d="M5 0a3.6 3.6 0 0 0-3.6 3.6C1.4 6.3 5 10 5 10s3.6-3.7 3.6-6.4A3.6 3.6 0 0 0 5 0zm0 5a1.4 1.4 0 1 1 0-2.8A1.4 1.4 0 0 1 5 5z"/></svg>
        <span>2450 N Harbor Way Suite 4<br>Coral Bay, FL 33401</span>
      </div>
      <div class="line"><svg viewBox="0 0 10 10"><path d="M3 0h4a1 1 0 0 1 1 1v8a1 1 0 0 1-1 1H3a1 1 0 0 1-1-1V1a1 1 0 0 1 1-1zm0 1.5v6.5h4V1.5z"/></svg><span>(555)201-4478 (Cell)</span></div>
      <div class="line"><svg viewBox="0 0 10 10"><path d="M2 0.5l2 2-1 1.2a6 6 0 0 0 3.3 3.3l1.2-1 2 2-1.3 1.5C4.6 9.5 0.5 5.4 0.5 1.8z"/></svg><span>(555)302-6610 Office</span></div>
      <div class="line"><svg viewBox="0 0 10 10"><path d="M2.5 0h5v3h-5zM0.5 3.5h9v4h-2V10h-5V7.5h-2zM3.5 6.5v2.5h3V6.5z"/></svg><span>(555)318-2290</span></div>
      <div class="line"><svg viewBox="0 0 10 10"><path d="M0.5 1.5h9v7h-9zm1 1v.3L5 5.3l3.5-2.5v-.3zm0 1.5v3.5h7V4L5 6.5z"/></svg><span>marco@Plumtarvessa.com</span></div>
      <div class="line web"><svg viewBox="0 0 10 10"><path d="M5 0.5a4.5 4.5 0 1 0 0 9 4.5 4.5 0 0 0 0-9zm-3.4 4h1.7c0-1 .2-1.9.5-2.6A3.5 3.5 0 0 0 1.6 4.5zm2.7 0h1.4c0-1.2-.3-2.3-.7-2.9-.4.6-.7 1.7-.7 2.9zm2.4 0h1.7a3.5 3.5 0 0 0-2.2-2.6c.3.7.5 1.6.5 2.6zM1.6 5.5a3.5 3.5 0 0 0 2.2 2.6c-.3-.7-.5-1.6-.5-2.6zm2.7 0c0 1.2.3 2.3.7 2.9.4-.6.7-1.7.7-2.9zm2.4 0c0 1-.2 1.9-.5 2.6a3.5 3.5 0 0 0 2.2-2.6z"/></svg><span>www.Plumtarvessa.com</span></div>
    </div>

    <div class="person">
      <p class="person-name">MARCO <em>VELLANI</em></p>
      <p class="person-role">SALES MANAGER</p>
    </div>

    <div class="brand-name">PLUMTARVESSA</div>
  </section>

</main>
</body>
</html>
```